Revelation Sanctuary Flyer

We need a flyer for a church seminar that focuses on the Revelation and the sanctuary, it will show images with giants, UFOs maybe some pyramids, sanctuary furniture pieces.

Front Cover, Middle and Back cover. size 8.5 x 11 folded in the middle
The information is in file 1 and file 2.
The other files are examples and ideas for layout.

Target Market(s)

Churches

Requirements
Must have
• 1. Flyer design files have to be print ready.
• 2. Must have appropriate bleed size and safe zone
• PDF, JPEG, PSD, AI, TIFF
Nice to have
• Images of Giants, UFO, Sanctuary building, Pyramids

```html
<!DOCTYPE html>
<html lang="en">
<head>
<meta charset="UTF-8">
<title>Sanctuary Furniture Seminar Flyer</title>
<link href="https://fonts.googleapis.com/css2?family=Roboto:wght@500;700;900&family=Lato:wght@400;700&display=swap" rel="stylesheet">
<style>
  :root {
    --page-bg: #d9d8d8;
    --panel-dark: #121110;
    --panel-mid: #1f1c1a;
    --text-light: #f4f1ec;
    --text-soft: #d8d2ca;
    --sky-glow: #b97a55;
    --sky-deep: #5a3a2c;
    --stone: #4a4038;
    --sun: #f5b35a;
  }
  * { margin: 0; padding: 0; box-sizing: border-box; }
  html, body { width: 1200px; height: 1200px; overflow: hidden; background: var(--page-bg); }
  .spread {
    position: absolute; left: 50px; top: 175px;
    width: 1100px; height: 850px;
    display: flex;
    box-shadow: 0 20px 50px rgba(0,0,0,.25);
  }
  .panel { position: relative; width: 550px; height: 850px; overflow: hidden; }

  /* Back panel */
  .back { background: var(--panel-dark); color: var(--text-light); font-family: "Lato", sans-serif; }
  .back-photo {
    position: absolute; left: 0; top: 0; width: 100%; height: 360px;
    background: linear-gradient(180deg, #2e2620 0%, #5b4a3a 45%, #3a2f27 75%, var(--panel-dark) 100%);
  }
  .hall-photo {
    position: absolute; left: 0; top: 470px; width: 100%; height: 380px;
    background: radial-gradient(ellipse at 55% 35%, #4b3f31 0%, #241d18 55%, var(--panel-dark) 100%);
    -webkit-mask-image: linear-gradient(180deg, transparent 0%, #000 30%);
    mask-image: linear-gradient(180deg, transparent 0%, #000 30%);
  }
  .back-content { position: absolute; left: 48px; right: 40px; top: 232px; }
  .invite { font-family: "Roboto", sans-serif; font-weight: 500; font-size: 19px; letter-spacing: .5px; }
  .headline {
    font-family: "Roboto", sans-serif; font-weight: 900; font-size: 36px;
    line-height: 1.02; text-transform: uppercase; margin-top: 8px;
  }
  .why { font-family: "Roboto", sans-serif; font-weight: 500; font-size: 17px; margin: 24px 0 0 14px; }
  .verse { font-size: 14px; line-height: 1.35; color: var(--text-soft); margin: 10px 0 0 0; }
  .answers { font-family: "Roboto", sans-serif; font-weight: 500; font-size: 17px; margin-top: 34px; line-height: 1.25; }
  .questions { list-style: none; margin-top: 12px; font-size: 14px; line-height: 1.35; color: var(--text-soft); }
  .questions li { display: flex; align-items: center; gap: 8px; }
  .questions svg { flex: none; }

  /* Front cover */
  .front { font-family: "Roboto", sans-serif; color: var(--text-light); }
  .cover-scene {
    position: absolute; inset: 0;
    background:
      radial-gradient(ellipse at 45% 8%, #f0c89a 0%, var(--sky-glow) 18%, transparent 45%),
      radial-gradient(ellipse at 48% 53%, var(--sun) 0%, rgba(245,179,90,.2) 12%, transparent 25%),
      linear-gradient(180deg, var(--sky-deep) 0%, #7b5240 25%, var(--stone) 50%, #2c2824 72%, var(--panel-mid) 100%);
  }
  .cover-title { position: absolute; left: 0; right: 0; top: 150px; text-align: center; }
  .presenter { font-weight: 700; font-size: 24px; line-height: 1.05; text-transform: uppercase; }
  .title {
    font-weight: 900; font-size: 66px; line-height: .98; text-transform: uppercase;
    margin-top: 4px; text-shadow: 0 3px 10px rgba(0,0,0,.35);
  }
  .dates {
    position: absolute; left: 0; right: 0; bottom: 60px; text-align: center;
    font-weight: 700; font-size: 30px; letter-spacing: .5px; text-transform: uppercase;
  }
</style>
</head>
<body>
  <main class="spread">
    <section class="panel back">
      <div class="back-photo" role="img" aria-label="Photo of a girl in a white dress leaning on a wooden balcony rail"></div>
      <div class="hall-photo" role="img" aria-label="Photo of an ornate hall with a glowing chandelier"></div>
      <div class="back-content">
        <p class="invite">WE INVITE YOU TO COME AS YOU ARE</p>
        <h2 class="headline">And discover hope<br>&amp; lasting peace<br>in these<br>trouble times</h2>
        <p class="why">WHY STUDY REVELATION?</p>
        <p class="verse">Blessed is he who reads and those who hear the words of this prophecy, and keep those things which are written in it; for the time is near.<br>Revelation 1:3</p>
        <p class="answers">- FIND ANSWERS TO YOUR<br>&nbsp;&nbsp;EVERYDAY QUESTIONS:</p>
        <ul class="questions">
          <li><svg width="14" height="10" viewBox="0 0 14 10"><path d="M0 5h11M7 1l4 4-4 4" stroke="#d8d2ca" stroke-width="1.6" fill="none"/></svg>What does the Bible say about the end of the world?</li>
          <li><svg width="14" height="10" viewBox="0 0 14 10"><path d="M0 5h11M7 1l4 4-4 4" stroke="#d8d2ca" stroke-width="1.6" fill="none"/></svg>Were there really Giants in the world?</li>
          <li><svg width="14" height="10" viewBox="0 0 14 10"><path d="M0 5h11M7 1l4 4-4 4" stroke="#d8d2ca" stroke-width="1.6" fill="none"/></svg>Are there UFO's?</li>
          <li><svg width="14" height="10" viewBox="0 0 14 10"><path d="M0 5h11M7 1l4 4-4 4" stroke="#d8d2ca" stroke-width="1.6" fill="none"/></svg>Why is there so much pain and suffering in the world?</li>
          <li><svg width="14" height="10" viewBox="0 0 14 10"><path d="M0 5h11M7 1l4 4-4 4" stroke="#d8d2ca" stroke-width="1.6" fill="none"/></svg>Is there life after death?</li>
          <li><svg width="14" height="10" viewBox="0 0 14 10"><path d="M0 5h11M7 1l4 4-4 4" stroke="#d8d2ca" stroke-width="1.6" fill="none"/></svg>Is Heaven and Hell real?</li>
        </ul>
      </div>
    </section>

    <section class="panel front">
      <div class="cover-scene" role="img" aria-label="Dramatic scene of standing stones at sunset under a lightning sky, with a pyramid and a camel in the foreground"></div>
      <div class="cover-title">
        <p class="presenter">Cedar Vale Fellowship<br>Presents</p>
        <h1 class="title">Sanctuary<br>Furniture</h1>
      </div>
      <p class="dates">May 19th - June 2nd, 2018</p>
    </section>
  </main>
</body>
</html>
```